Facebook Header Design Project.

I'm supplying white and colored logos. The Facebook page already exists. URL = https://www.pagebook.example/lumocrest.design The design should not be based on what's already there. Consider mobile implications of the design. This Design will form the designs of other social media headers. LumoCrest is a web design | digital marketing company.

Target Market(s)

People interested in web design | digital marketing services.

Industry/Entity Type

LumoCrest is a web design | digital marketing company. That should be clear in the design.

Colors
0054AA
0677BA
7BADD7
CADEEF
E8F1F8

Requirements
Must have
• Logo. Use Facebook header image dimension.
Nice to have
• Use a color scheme like the logo and feel free to add a color or two from the other side of the color whee.

```html
<!DOCTYPE html>
<html lang="en">
<head>
<meta charset="utf-8">
<title>LumoCrest – Page Header</title>
<link rel="stylesheet" href="https://fonts.googleapis.com/css2?family=Montserrat:wght@400;500;700&display=swap">
<style>
  :root {
    --sky: #2873fb;
    --violet: #5d21d0;
    --indigo-mid: #3d4fe6;
    --navy: #3a4f91;
    --brand-blue: #0677BA;
    --pale: rgba(232, 241, 248, 0.9);
    --mist: rgba(202, 222, 239, 0.75);
    --clear: rgba(255, 255, 255, 0);
    --white: #ffffff;
  }
  * { margin: 0; padding: 0; box-sizing: border-box; }
  html, body { width: 1200px; height: 1018px; overflow: hidden; }
  body {
    position: relative;
    font-family: "Montserrat", sans-serif;
    background: linear-gradient(180deg, var(--sky) 0%, var(--sky) 64%, var(--indigo-mid) 80%, var(--violet) 100%);
  }
  .cover {
    position: absolute;
    left: 98px; top: 306px;
    width: 1004px; height: 372px;
    background: var(--white);
    box-shadow: 0 14px 24px rgba(10, 20, 60, 0.35);
    overflow: hidden;
  }
  .cover__pattern {
    position: absolute;
    top: 0; height: 100%;
  }
  .cover__pattern--left {
    left: 0; width: 600px;
    background: linear-gradient(90deg, var(--mist) 0%, var(--pale) 55%, var(--clear) 100%);
  }
  .cover__pattern--right {
    right: 0; width: 200px;
    background: linear-gradient(270deg, var(--mist) 0%, var(--pale) 55%, var(--clear) 100%);
  }
  .cover__brand {
    position: absolute;
    left: 0; right: 0; top: 112px;
    text-align: center;
  }
  .cover__name {
    font-weight: 700;
    font-size: 84px;
    letter-spacing: 1px;
    color: var(--navy);
    line-height: 1;
  }
  .cover__tagline {
    margin-top: 36px;
    font-weight: 500;
    font-size: 22px;
    color: var(--navy);
  }
  .profile {
    position: absolute;
    left: 121px; top: 666px;
    width: 110px; height: 110px;
    border-radius: 50%;
    background: var(--white);
    border: 3px solid var(--brand-blue);
    box-shadow: 0 6px 14px rgba(10, 20, 60, 0.35);
    display: flex; align-items: center; justify-content: center;
  }
  .profile__name {
    font-weight: 700;
    font-size: 16px;
    color: var(--brand-blue);
  }
  .page-title {
    position: absolute;
    left: 258px; top: 712px;
    color: var(--white);
  }
  .page-title__name {
    font-weight: 700;
    font-size: 29px;
    line-height: 1;
  }
  .page-title__meta {
    margin-top: 2px;
    font-size: 9px;
    font-weight: 400;
  }
</style>
</head>
<body>
  <section class="cover">
    <div class="cover__pattern cover__pattern--left" role="img" aria-label="Light blue geometric cube pattern"></div>
    <div class="cover__pattern cover__pattern--right" role="img" aria-label="Light blue geometric cube pattern"></div>
    <div class="cover__brand">
      <div class="cover__name">LumoCrest</div>
      <div class="cover__tagline">Web Design | Digital Marketing Company</div>
    </div>
  </section>

  <div class="profile"><span class="profile__name">LumoCrest</span></div>

  <div class="page-title">
    <div class="page-title__name">LumoCrest</div>
    <div class="page-title__meta">@lumocrest.design &nbsp;· Creador digital</div>
  </div>
</body>
</html>
```